BrightMesa Business Card Contest

We are looking for a modern business card that catches attention and is unique. Attached is the brand guide and logo files. Please note that the back side (not the side with our name and info) with be UV raise printed, so have fun with the design there. We want to include Name, Title, Phone number, email, website.

Contact Information for Business Card

Please see project description

```html
<!DOCTYPE html>
<html lang="en">
<head>
<meta charset="utf-8">
<title>BrightMesa Business Card</title>
<link rel="stylesheet" href="https://fonts.googleapis.com/css2?family=Nunito+Sans:wght@400;600;800&display=swap">
<style>
  :root {
    --backdrop: #282b30;
    --card: #212226;
    --card-glow: #26282d;
    --ink: #ffffff;
    --accent: #2f7cc4;
    --bright: #27c1ea;
  }
  * { margin: 0; padding: 0; box-sizing: border-box; }
  html, body {
    width: 1200px;
    height: 1000px;
    overflow: hidden;
    background: var(--backdrop);
    font-family: "Nunito Sans", sans-serif;
    color: var(--ink);
  }
  .card {
    position: absolute;
    left: 290px;
    width: 620px;
    height: 355px;
    background: var(--card);
    overflow: hidden;
  }
  .card--front { top: 118px; }
  .card--back {
    top: 527px;
    background: radial-gradient(circle at 50% 50%, var(--card-glow) 0, var(--card) 110px);
  }

  .brand {
    position: absolute;
    left: 44px;
    top: 48px;
    display: flex;
    align-items: center;
    gap: 10px;
  }
  .brand-square {
    width: 42px;
    height: 42px;
    background: var(--bright);
    flex: none;
  }
  .brand-name {
    font-size: 44px;
    font-weight: 600;
    line-height: 1;
    letter-spacing: -0.01em;
    color: var(--ink);
  }
  .person-name {
    position: absolute;
    left: 44px;
    top: 278px;
    top: 160px;
    font-size: 31px;
    font-weight: 800;
    line-height: 1;
  }
  .person-title {
    position: absolute;
    left: 44px;
    top: 200px;
    font-size: 16px;
    font-weight: 400;
    letter-spacing: 0.14em;
    text-transform: uppercase;
    color: var(--accent);
    line-height: 1;
  }
  .divider {
    position: absolute;
    left: 44px;
    top: 235px;
    width: 64px;
    height: 2px;
    background: var(--accent);
  }
  .contact {
    position: absolute;
    display: flex;
    align-items: center;
    gap: 10px;
    font-size: 19px;
    font-weight: 400;
    line-height: 1;
  }
  .contact svg { width: 19px; height: 19px; fill: var(--accent); flex: none; }
  .contact--phone { left: 44px; top: 258px; }
  .contact--email { left: 267px; top: 258px; }
  .contact--web { left: 44px; top: 290px; }

  .back-brand {
    position: absolute;
    inset: 0;
    display: flex;
    align-items: center;
    justify-content: center;
    gap: 16px;
  }
  .back-square {
    width: 60px;
    height: 60px;
    border: 2px solid var(--bright);
    flex: none;
  }
  .back-name {
    font-size: 52px;
    font-weight: 600;
    line-height: 1;
    color: var(--ink);
  }
</style>
</head>
<body>
  <section class="card card--front">
    <div class="brand">
      <span class="brand-square" aria-hidden="true"></span>
      <span class="brand-name">BrightMesa</span>
    </div>
    <h1 class="person-name">Dana Reyes</h1>
    <p class="person-title">Senior Solutions Architect</p>
    <div class="divider"></div>
    <p class="contact contact--phone">
      <svg viewBox="0 0 24 24" aria-hidden="true"><path d="M6.6 10.8a15.2 15.2 0 0 0 6.6 6.6l2.2-2.2c.3-.3.7-.4 1-.2 1.1.4 2.3.6 3.6.6.6 0 1 .4 1 1V20c0 .6-.4 1-1 1A17 17 0 0 1 3 4c0-.6.4-1 1-1h3.5c.6 0 1 .4 1 1 0 1.3.2 2.5.6 3.6.1.3 0 .7-.2 1l-2.3 2.2z"/></svg>
      +1 (555) 014-2290
    </p>
    <p class="contact contact--email">
      <svg viewBox="0 0 24 24" aria-hidden="true"><path d="M2 5h20v14H2z"/><path d="M3 6l9 7 9-7" fill="none" stroke="var(--card)" stroke-width="1.4"/><path d="M3 18l6.5-6M21 18l-6.5-6" stroke="var(--card)" stroke-width="1.2"/></svg>
      dana@brightmesa.com
    </p>
    <p class="contact contact--web">
      <svg viewBox="0 0 24 24" aria-hidden="true"><circle cx="12" cy="12" r="10"/><path d="M2 12h20M12 2v20M4 7h16M4 17h16M12 2c-4 4-4 16 0 20M12 2c4 4 4 16 0 20" fill="none" stroke="var(--card)" stroke-width="1.2"/></svg>
      www.brightmesa.com
    </p>
  </section>

  <section class="card card--back">
    <div class="back-brand">
      <span class="back-square" aria-hidden="true"></span>
      <span class="back-name">BrightMesa</span>
    </div>
  </section>
</body>
</html>
```